Corvane Supplies Business Card

Professional business card that stand out to our potential customers. Front and back with clean modern design

Industry/Entity Type

Oil and gas

Contact Information for Business Card

Name, address, website , office phone and cell number

Requirements
Must have
• Editable files for each employee

```html
<!DOCTYPE html>
<html lang="en">
<head>
<meta charset="utf-8">
<title>Corvane Supplies Business Card</title>
<link rel="stylesheet" href="https://fonts.googleapis.com/css2?family=Nunito+Sans:wght@400;800&display=swap">
<style>
  :root {
    --brand-red: #ee1f27;
    --brand-blue: #0fb0d2;
    --ink: #1d1d1d;
    --card: #ffffff;
    --backdrop: #a3a3a3;
  }
  * { margin: 0; padding: 0; box-sizing: border-box; }
  html, body { width: 1199px; height: 1200px; overflow: hidden; }
  body {
    background: var(--backdrop);
    font-family: "Nunito Sans", Arial, sans-serif;
    position: relative;
  }
  .card {
    position: absolute;
    left: 166px;
    width: 866px;
    height: 508px;
    background: var(--card);
    overflow: hidden;
  }
  .card--front { top: 67px; }
  .card--back { top: 612px; }

  .front-accent { position: absolute; inset: 0; }

  .brand-name {
    position: absolute;
    color: var(--brand-red);
    font-weight: 800;
    text-transform: uppercase;
    letter-spacing: 1px;
    text-align: center;
    line-height: 1.1;
  }
  .card--front .brand-name {
    left: 90px; top: 205px; width: 240px;
    font-size: 38px;
  }
  .card--back .brand-name {
    left: 0; width: 866px; top: 218px;
    font-size: 50px;
  }

  .holder {
    position: absolute;
    right: 80px; top: 212px;
    white-space: nowrap;
  }
  .holder__name {
    color: var(--brand-red);
    font-weight: 800;
    font-size: 30px;
    letter-spacing: 0.5px;
  }
  .holder__role {
    color: var(--ink);
    font-size: 22px;
    font-weight: 400;
  }
  .holder__slash { color: var(--ink); font-size: 30px; font-weight: 400; }

  .contact-list {
    position: absolute;
    right: 60px;
    top: 290px;
    list-style: none;
    text-align: right;
  }
  .contact-list li {
    display: flex;
    justify-content: flex-end;
    align-items: center;
    gap: 14px;
    font-size: 21px;
    color: var(--ink);
    height: 33.5px;
  }
  .contact-list li.contact--web { color: var(--brand-red); font-weight: 800; }
  .contact-list li.contact--address { margin-top: 20px; }
  .contact-list svg { width: 18px; height: 18px; flex: none; }
</style>
</head>
<body>

<section class="card card--front">
  <svg class="front-accent" width="866" height="508" viewBox="0 0 866 508">
    <polygon points="477,0 866,0 866,222" fill="var(--brand-blue)"/>
    <polyline points="355,-14 540,90 795,90 890,138" fill="none" stroke="#ffffff" stroke-width="34"/>
    <polyline points="355,-14 540,88 795,88 890,136" fill="none" stroke="var(--brand-red)" stroke-width="19"/>
  </svg>

  <div class="brand-name">Corvane<br>Supplies</div>

  <div class="holder">
    <span class="holder__name">MAREN OKAFOR</span>
    <span class="holder__slash">/</span>
    <span class="holder__role">Owner</span>
  </div>

  <ul class="contact-list">
    <li>555.210.4477
      <svg viewBox="0 0 18 18"><rect x="5" y="1.5" width="8" height="15" rx="1.5" fill="none" stroke="var(--brand-blue)" stroke-width="1.6"/><line x1="8" y1="14" x2="10" y2="14" stroke="var(--brand-blue)" stroke-width="1.4"/></svg>
    </li>
    <li>info@corvanesupplies.com
      <svg viewBox="0 0 18 18"><rect x="2" y="4" width="14" height="10" rx="1" fill="var(--brand-blue)"/><polyline points="2.5,4.5 9,9.5 15.5,4.5" fill="none" stroke="#fff" stroke-width="1.3"/></svg>
    </li>
    <li class="contact--web">www.corvanesupplies.com
      <svg viewBox="0 0 18 18"><circle cx="9" cy="9" r="7" fill="none" stroke="var(--brand-red)" stroke-width="1.6"/><ellipse cx="9" cy="9" rx="3" ry="7" fill="none" stroke="var(--brand-red)" stroke-width="1.3"/><line x1="2" y1="9" x2="16" y2="9" stroke="var(--brand-red)" stroke-width="1.3"/></svg>
    </li>
    <li class="contact--address">000 Harbor Ln, Westvale, FL 30000
      <svg viewBox="0 0 18 18"><path d="M9 17 C5 11.5 3.5 9 3.5 6.5 a5.5 5.5 0 0 1 11 0 C14.5 9 13 11.5 9 17z" fill="var(--brand-blue)"/><circle cx="9" cy="6.5" r="2" fill="#fff"/></svg>
    </li>
  </ul>
</section>

<section class="card card--back">
  <div class="brand-name">Corvane Supplies</div>
</section>

</body>
</html>
```